Kveldbrá - Start-up company selling electricity

Hello let me tell you about Kveldbrá.

Kveldbrá is start-up company selling electricity in Iceland. The operations of the company consist of making power usage forecasts for our customers, purchasing the electricity wholesale from the energy producers, and selling the electricity to the consumer. We are focused on tech by using optimization and machine learning to minimize electricity prices to our customers. Our marketing strategy is to portray a tech company mindset and to show dedication to driving down the electricity price on the market.

We need your help to make our website pop. Possible concepts to work with are as follows:

- Iceland the land of ice and fire
- Green energy
- Innovation
- Tech and data science

Link to our website: https://prufa.kveldbra.is/
We are open to ideas.
Thank you!

Target Market(s)

Electricity consumers both homes and companies.

Number of Pages Required

1 page

Font styles to use
Serif
Sans Serif

```html
<!DOCTYPE html>
<html lang="en">
<head>
<meta charset="utf-8">
<title>Kveldbrá – Selling and Generating Energy in Iceland</title>
<link href="https://fonts.googleapis.com/css2?family=Noto+Serif:wght@400;700&family=Source+Sans+3:wght@400;600&family=Rubik:wght@600&family=Montserrat:wght@400&display=swap" rel="stylesheet">
<style>
:root{
  --navy-deep:#151a24;
  --navy:#1e2430;
  --navy-panel:#212836;
  --red:#b0322a;
  --red-band:#a8302a;
  --blue-btn:#1f3a6b;
  --text:#ffffff;
  --muted:#c9ccd3;
  --line:#2c3342;
}
*{margin:0;padding:0;box-sizing:border-box}
html,body{width:1200px;height:2715px;overflow:hidden;background:var(--navy-deep);color:var(--text);font-family:"Source Sans 3",sans-serif}
.page{position:relative;width:1200px;height:2715px}
section,header,footer{position:absolute;left:0;width:1200px}
.btn{display:inline-block;font-family:"Noto Serif",serif;font-size:15px;color:#fff;border-radius:20px;padding:9px 22px;text-decoration:none;letter-spacing:.3px}
.btn-red{background:var(--red)}
.btn-blue{background:var(--blue-btn)}
.heading{border-left:2px solid var(--red);padding-left:16px;font-family:"Noto Serif",serif;font-weight:400}
.brand{display:flex;align-items:center;gap:10px;font-family:"Noto Serif",serif;font-size:26px;color:var(--red)}
.brand-dot{width:22px;height:22px;border-radius:50%;background:var(--red)}

/* header */
.site-header{top:0;height:75px;background:var(--navy-deep);display:flex;align-items:center;justify-content:space-between;padding:0 60px}
.nav{display:flex;align-items:center;gap:20px;font-size:13px;color:#d9dbe0}
.lang{background:var(--red);border-radius:13px;padding:4px 12px;font-size:12px}

/* hero */
.hero{top:75px;height:637px}
.hero-photo{position:absolute;inset:0;background:linear-gradient(180deg,#2a3350 0%,#3a4462 35%,#4a3d3a 62%,#1b2230 100%)}
.hero-content{position:absolute;top:170px;width:100%;text-align:center}
.hero h1{font-family:"Rubik",sans-serif;font-weight:600;font-size:50px;line-height:57px;text-shadow:0 2px 6px rgba(0,0,0,.5)}
.hero-sub{display:inline-block;margin-top:12px;background:rgba(20,24,36,.55);padding:7px 26px;font-family:"Montserrat",sans-serif;font-size:14px}
.hero-actions{margin-top:24px;display:flex;justify-content:center;gap:12px}
.hero-actions .btn{padding:11px 22px}
.arrow{position:absolute;top:270px;width:36px;height:60px}
.arrow.left{left:0}.arrow.right{right:0}

/* unique */
.unique{top:712px;height:390px;background:var(--navy-deep)}
.unique .heading{position:absolute;left:143px;top:67px;font-size:27px;line-height:38px;width:580px}
.unique p{position:absolute;left:159px;top:156px;width:560px;font-size:13px;line-height:21px;color:var(--muted)}
.unique .btn{position:absolute;left:160px;top:276px}
.unique-deco{position:absolute;left:836px;top:190px;width:200px;height:200px;border-radius:50%;background:#1a2334}

/* split rows */
.row{height:322px;display:flex}
.row > div{width:600px;height:100%;position:relative}
.panel{background:var(--navy-panel)}
.row1{top:1102px}.row2{top:1424px}.row3{top:1747px}
.photo-pylons{background:linear-gradient(180deg,#3b86b8 0%,#7f8ea0 55%,#d98752 85%,#e59a5e 100%)}
.photo-man{background:linear-gradient(135deg,#e8e6e2 0%,#c8c1b8 55%,#9c8e80 100%)}
.photo-network{background:linear-gradient(160deg,#1a2a7a 0%,#223694 50%,#141c44 100%)}
.panel .heading{font-weight:700;font-size:24px}
.welcome .heading{position:absolute;left:74px;top:102px}
.welcome p{position:absolute;left:88px;top:140px;width:360px;font-size:13.5px;line-height:20px;color:var(--muted)}
.welcome .actions{position:absolute;left:89px;top:198px;display:flex;gap:8px}
.prices .heading{position:absolute;left:212px;top:66px}
.price-list{position:absolute;left:231px;top:110px}
.price{display:flex;align-items:baseline;gap:8px;height:34px}
.price b{font-family:"Noto Serif",serif;font-weight:400;font-size:25px;color:var(--red)}
.price span{font-size:12px;color:#d8dae0}
.prices .label{position:absolute;left:231px;top:191px;font-size:13px;color:var(--muted)}
.prices .link{position:absolute;left:230px;top:213px;font-size:15px}
.future .heading{position:absolute;left:74px;top:100px}
.future p{position:absolute;left:91px;top:140px;width:340px;font-size:13.5px;line-height:20px;color:var(--muted)}

/* band */
.choose{top:2068px;height:335px;background:radial-gradient(circle at 75% 45%,#b8382d 0%,var(--red-band) 40%,#9b2b25 100%);text-align:center}
.choose h2{margin-top:122px;font-family:"Noto Serif",serif;font-weight:400;font-size:28px}
.choose h2 strong{font-weight:700}
.choose p{margin:14px auto 0;width:680px;font-size:13.5px;line-height:21px;color:#f3dcda}
.choose .btn{margin-top:18px;padding:9px 25px}

/* footer */
.site-footer{top:2403px;height:312px;background:var(--navy-deep)}
.site-footer .brand{position:absolute;left:484px;top:64px}
.footer-cols{position:absolute;left:240px;top:125px;width:720px;display:flex}
.footer-col{height:130px;padding-top:10px;font-size:11.5px;color:var(--muted)}
.footer-col + .footer-col{border-left:1px solid var(--line)}
.col-links{width:230px;padding-left:20px}
.col-contact{width:258px;padding-left:26px}
.col-company{width:232px;padding-left:26px}
.footer-col li{list-style:none;display:flex;align-items:center;gap:14px;height:25px}
.col-links li::before,.col-company li::before{content:"";width:4px;height:4px;border-radius:50%;background:var(--red)}
.col-contact li{height:29px;gap:12px}
.col-contact svg{width:15px;height:15px;fill:var(--red)}
.col-contact .phone{font-size:16px}
.copyright{position:absolute;left:240px;top:2666px;width:720px;border-top:1px solid var(--line);text-align:center;font-size:11.5px;color:var(--muted);padding-top:20px}
</style>
</head>
<body>
<div class="page">

<header class="site-header">
  <div class="brand"><span class="brand-dot"></span>KVELDBRÁ</div>
  <nav class="nav">
    <span>Terms of Business</span><span>Question &amp; Answer</span><span>About Kveldbrá</span>
    <span class="lang">En ▾</span>
  </nav>
</header>

<section class="hero">
  <div class="hero-photo" role="img" aria-label="Night view of an Icelandic city with an electricity pylon in the foreground"></div>
  <svg class="arrow left" viewBox="0 0 36 60"><path d="M0 0 L36 30 L0 60Z" fill="#b0322a"/><path d="M18 22 L11 30 L18 38" stroke="#fff" stroke-width="2" fill="none"/></svg>
  <svg class="arrow right" viewBox="0 0 36 60"><path d="M36 0 L0 30 L36 60Z" fill="#b0322a"/><path d="M18 22 L25 30 L18 38" stroke="#fff" stroke-width="2" fill="none"/></svg>
  <div class="hero-content">
    <h1>Kveldbrá Selling and<br>Generating Energy In Iceland</h1>
    <div class="hero-sub">Everything you need to know About How we Can Help you sell Electricity</div>
    <div class="hero-actions"><a class="btn btn-red">REGISTER NOW</a><a class="btn btn-blue">GET A QUOTE</a></div>
  </div>
</section>

<section class="unique">
  <div class="unique-deco"></div>
  <h2 class="heading">What is Kveldbrá's Unique Position in the Electricity Sales Market?</h2>
  <p>Kveldbrá uses automation and artificial intelligence to achieve lower prices in the electricity market. Our goal is to minimize the cost of energy sales, promote energy balance and offer good service. Kveldbrá's goal is to offer its customers the most favorable electricity prices in Iceland. Electricity is part of the monthly costs of households and companies, and by doing business with Kveldbrá, savings can be achieved and operating costs reduced.</p>
  <a class="btn btn-red">LEARN MORE</a>
</section>

<section class="row row1">
  <div class="photo-pylons" role="img" aria-label="Power line pylons against a sunset sky"></div>
  <div class="panel welcome">
    <h2 class="heading">Welcome To Business</h2>
    <p>it can be said that by trading with Kveldbrá, you support the development of the Icelandic electricity market.</p>
    <div class="actions"><a class="btn btn-red">REGISTER</a><a class="btn btn-blue">COMPANY</a></div>
  </div>
</section>

<section class="row row2">
  <div class="panel prices">
    <h2 class="heading">Price List</h2>
    <div class="price-list">
      <div class="price"><b>6.95</b><span>ISK/kWh</span></div>
      <div class="price"><b>6.22</b><span>ISK/kWh</span></div>
    </div>
    <div class="label">Electric Acceleration</div>
    <div class="link">Make a price comparison</div>
  </div>
  <div class="photo-man" role="img" aria-label="Man working thoughtfully at a laptop in a bright room"></div>
</section>

<section class="row row3">
  <div class="photo-network" role="img" aria-label="Glowing network of connected device icons over a night city"></div>
  <div class="panel future">
    <h2 class="heading">The Future Is Exciting</h2>
    <p>Let's make the electricity system smarter together. Kveldbrá uses artificial intelligence, data science and automation to minimize costs and promote eccentricity</p>
  </div>
</section>

<section class="choose">
  <h2>You Choose Where You <strong>Buy Electricity</strong></h2>
  <p>Did you know that you can decide where to buy electricity for your home, regardless of location? Here you can see an independent price comparison of all electricity sales and switch to more favorable electricity.</p>
  <a class="btn btn-blue">VERÐVAKI</a>
</section>

<footer class="site-footer">
  <div class="brand"><span class="brand-dot"></span>KVELDBRÁ</div>
  <div class="footer-cols">
    <ul class="footer-col col-links">
      <li>Terms of Business</li><li>Question &amp; Answer</li><li>About Kveldbrá</li>
    </ul>
    <ul class="footer-col col-contact">
      <li><svg viewBox="0 0 16 16"><path d="M8 0a5.5 5.5 0 0 0-5.5 5.5C2.5 10 8 16 8 16s5.5-6 5.5-10.5A5.5 5.5 0 0 0 8 0zm0 8a2.5 2.5 0 1 1 0-5 2.5 2.5 0 0 1 0 5z"/></svg>Hafnargata 21 220 Hafnarfjörður</li>
      <li><svg viewBox="0 0 16 16"><path d="M0 3h16v10H0z M0 3l8 6 8-6" /></svg>hallo@kveldbra.is</li>
      <li class="phone"><svg viewBox="0 0 16 16"><path d="M3 0l3 4-2 2c1 2 4 5 6 6l2-2 4 3-2 3C7 16 0 9 0 2z"/></svg>410-2020</li>
    </ul>
    <ul class="footer-col col-company">
      <li>Kveldbrá ehf</li><li>ID number: 510371-0284</li><li>VAT number: 207164</li>
    </ul>
  </div>
</footer>
<div class="copyright">©<strong>Kveldbrá</strong> - 2021 all right rserved.</div>

</div>
</body>
</html>
```